Willow Glow & Laser - Business Banner with Brand Elements

Design:
• We would like to get a creative design for a wide banner that will go outside our medical spa clinic location. We need a designer to make a simple yet colorful and high-quality design layout. We want this banner to be eye-catching and to communicate the services we offer at our business: Laser Hair Removal | Velonix | Lip Filler.

Requirements:
• We would like the banner to include our companies information which is the following:

Logo
“Refresh Your Skin”
Laser Hair Removal | Velonix | Lip Filler
(555) 287-1936
www.WillowGlowLaser.com

Colors:
• Our business colors are orange, a hint of black and white, but mostly peach/orange tones. (Orange: #f78f20 , White: #ffffff)

Fonts:
• Josefins Sans Bold & Lato

Content and images can be located here:
https://files.cloudvaultshare.com/folders/7tQmZ2xVbR9kLpN4sW8yH3cD6fJ1gA0eU?usp=sharing

The following will give you an idea of our brand presentation:
• Our website is: www.WillowGlowLaser.com
• Our Instagram; @willowglowlaser
• Our Facebook: www.socialpagehub.com/willowglowlaser

Target Market(s)
• Women 25 - 45

Industry/Entity Type
• Beauty

```html
<!DOCTYPE html>
<html lang="en">
<head>
<meta charset="utf-8">
<title>Willow Glow &amp; Laser – Banner</title>
<link rel="stylesheet" href="https://fonts.googleapis.com/css2?family=Poppins:wght@600;700&family=Josefin+Sans:wght@400;600&display=swap">
<style>
  :root {
    --orange: #f7a035;
    --orange-deep: #f78f20;
    --ink: #141414;
    --white: #ffffff;
    --mist: #f2f2f2;
    --photo-cool: #9fd3e8;
    --photo-warm: #e6d9c8;
  }
  * { margin: 0; padding: 0; box-sizing: border-box; }
  html, body { width: 1200px; height: 457px; overflow: hidden; background: var(--white); }
  .banner {
    position: relative;
    width: 1200px;
    height: 457px;
    overflow: hidden;
    background: var(--white);
    font-family: "Josefin Sans", sans-serif;
    color: var(--ink);
  }
  .backdrop-photo {
    position: absolute;
    left: 230px;
    top: 0;
    width: 430px;
    height: 457px;
    background: radial-gradient(ellipse at 45% 40%, #d9d9d9 0%, #ececec 45%, rgba(255,255,255,0) 75%);
    opacity: .8;
  }
  .hero-art { position: absolute; inset: 0; }
  .brand {
    position: absolute;
    left: 44px;
    top: 80px;
    display: flex;
    align-items: center;
    gap: 14px;
  }
  .brand-dot {
    width: 46px;
    height: 46px;
    border-radius: 50%;
    background: var(--orange);
  }
  .brand-name {
    font-family: "Poppins", sans-serif;
    font-weight: 700;
    font-size: 34px;
    color: var(--ink);
    letter-spacing: -0.3px;
  }
  .headline {
    position: absolute;
    left: 42px;
    top: 188px;
    font-family: "Poppins", sans-serif;
    font-weight: 700;
    font-size: 58px;
    line-height: 1;
    letter-spacing: -1px;
    color: var(--ink);
    white-space: nowrap;
  }
  .headline .accent { color: var(--orange); }
  .services {
    position: absolute;
    left: 44px;
    top: 264px;
    font-size: 22px;
    color: var(--ink);
    white-space: nowrap;
  }
  .contacts {
    position: absolute;
    left: 44px;
    top: 332px;
    display: flex;
    gap: 30px;
    font-size: 24px;
    color: var(--ink);
    white-space: nowrap;
  }
  .contact { display: flex; align-items: center; gap: 12px; }
  .contact-icon {
    width: 26px;
    height: 26px;
    border-radius: 6px;
    background: var(--orange);
    display: flex;
    align-items: center;
    justify-content: center;
  }
  .contact-text { padding-top: 3px; }
</style>
</head>
<body>
<main class="banner">
  <div class="backdrop-photo" role="img" aria-label="Faded greyscale photo of a smiling woman at the beach"></div>

  <svg class="hero-art" width="1200" height="457" viewBox="0 0 1200 457">
    <defs>
      <linearGradient id="photo-tone" x1="0" y1="0" x2="1" y2="1">
        <stop offset="0" stop-color="var(--photo-cool)"/>
        <stop offset="1" stop-color="var(--photo-warm)"/>
      </linearGradient>
    </defs>
    <circle class="accent-ring" cx="1024" cy="205" r="439" fill="var(--orange)"/>
    <circle class="photo-window" cx="1053" cy="219" r="373" fill="url(#photo-tone)" role="img" aria-label="Photo of a smiling woman in a straw hat on a sunny beach"/>
  </svg>

  <div class="brand">
    <span class="brand-dot"></span>
    <span class="brand-name">Willow Glow &amp; Laser</span>
  </div>

  <h1 class="headline"><span class="accent">Refresh</span> Your Skin</h1>

  <p class="services">Laser Hair Removal | Velonix | Lip Filler</p>

  <div class="contacts">
    <div class="contact">
      <span class="contact-icon">
        <svg width="16" height="16" viewBox="0 0 24 24"><path fill="#fff" d="M6.6 10.8a15.1 15.1 0 0 0 6.6 6.6l2.2-2.2a1 1 0 0 1 1-.25 11.4 11.4 0 0 0 3.6.57 1 1 0 0 1 1 1V20a1 1 0 0 1-1 1A17 17 0 0 1 3 4a1 1 0 0 1 1-1h3.5a1 1 0 0 1 1 1c0 1.25.2 2.45.57 3.57a1 1 0 0 1-.25 1z"/></svg>
      </span>
      <span class="contact-text">(555) 287-1936</span>
    </div>
    <div class="contact">
      <span class="contact-icon">
        <svg width="16" height="16" viewBox="0 0 24 24" fill="none" stroke="#fff" stroke-width="2.6" stroke-linecap="round"><path d="M10 14a4 4 0 0 0 5.7 0l3-3a4 4 0 0 0-5.7-5.7l-1 1"/><path d="M14 10a4 4 0 0 0-5.7 0l-3 3a4 4 0 0 0 5.7 5.7l1-1"/></svg>
      </span>
      <span class="contact-text">www.WillowGlowLaser.com</span>
    </div>
  </div>
</main>
</body>
</html>
```